Website Revamp: Favorzo.com

Just got a new logo looking for a web design to go with the business. I need the photoshop files and stock photos. No Word Press Please.

```html
<!DOCTYPE html>
<html lang="en">
<head>
<meta charset="utf-8">
<title>Favorzo – Sell your car quickly</title>
<link href="https://fonts.googleapis.com/css2?family=Open+Sans:wght@300;400;600;700&display=swap" rel="stylesheet">
<style>
:root{
  --green:#8dc63f;
  --green-light:#c4e295;
  --grey:#838c8c;
  --text:#666;
  --dark:#2b2b2b;
  --darker:#1e1e1e;
  --white:#fff;
  --line:#ddd;
}
*{box-sizing:border-box;margin:0;padding:0}
html,body{width:1200px;height:3335px;overflow:hidden}
body{position:relative;font-family:"Open Sans",Arial,sans-serif;color:var(--text);background:var(--white)}
.abs{position:absolute}
/* top bar */
.topbar{left:0;top:0;width:1200px;height:40px;background:var(--green);color:var(--white);font-size:14px}
.topbar .contact-item{position:absolute;top:10px;display:flex;align-items:center;gap:8px}
.social{position:absolute;top:11px;display:flex;gap:12px}
.social span{display:block;width:17px;height:17px;background:var(--white);border-radius:3px}
.topbar .login{position:absolute;left:942px;top:12px;font-size:11px}
.topbar .register{position:absolute;left:1016px;top:5px;width:84px;height:29px;border:1px solid var(--white);font-size:11px;display:flex;align-items:center;justify-content:center}
/* header */
.logo{display:flex;flex-direction:column;align-items:center;gap:2px}
.logo .mark{width:56px;height:56px;border-radius:50%;background:var(--green)}
.logo .name{font-weight:700;font-size:20px;color:var(--green)}
.nav{left:448px;top:90px;font-size:16px;color:#777;display:flex}
.nav a{position:absolute;white-space:nowrap;text-decoration:none;color:inherit}
.nav .active{color:var(--green)}
.btn-offer{left:984px;top:83px;width:116px;height:36px;background:var(--green);color:var(--white);font-size:16px;display:flex;align-items:center;justify-content:center}
/* hero */
.hero{left:0;top:159px;width:1200px;height:670px;background:linear-gradient(180deg,#b9c7c9 0%,#4f6b3a 35%,#3f5a2a 60%,#6b7b4e 100%)}
.hero-car{left:500px;top:300px;width:590px;height:290px;border-radius:45% 40% 20% 20%;background:linear-gradient(180deg,#f6f7f7,#d7dadb)}
.hero-title{left:117px;top:218px;font-size:36px;font-weight:300;color:var(--white)}
.field{background:var(--white);color:#999;font-size:16px;padding-left:18px;display:flex;align-items:center;justify-content:space-between;padding-right:18px}
.field .caret{width:0;height:0;border-left:6px solid transparent;border-right:6px solid transparent;border-top:9px solid #888}
.btn-quote{left:117px;top:545px;width:151px;height:48px;background:var(--green);color:var(--white);font-size:16px;display:flex;align-items:center;justify-content:center}
/* cash offers */
.section-title{font-weight:300;font-size:38px;color:#777}
.rule{height:2px;background:#bbb}
.card{top:950px;width:208px;height:300px;border:1px solid var(--line);background:var(--white)}
.card .photo{position:absolute;left:16px;top:16px;width:174px;height:130px}
.card .title{position:absolute;left:19px;top:157px;font-size:17px;color:#666}
.card .loc{position:absolute;left:19px;top:180px;font-size:15px;color:#999;display:flex;gap:6px;align-items:center}
.card .stars{position:absolute;left:19px;top:203px;font-size:15px;letter-spacing:3px;color:#e4e71b}
.card .stars b{color:#888;font-weight:400}
.card .sep{position:absolute;left:16px;right:16px;top:230px;height:1px;background:var(--line)}
.card .meta{position:absolute;left:19px;top:260px;font-size:7px;color:#777;line-height:13px}
.card .price{position:absolute;left:93px;top:243px;width:97px;height:40px;background:var(--green);color:var(--white);font-size:31px;font-weight:600;display:flex;align-items:center;justify-content:center}
.card .price sup{font-size:13px;margin-right:5px;align-self:flex-start;margin-top:6px}
.arrow{width:24px;height:48px}
/* difference */
.difference{left:0;top:1349px;width:1200px;height:613px;background:var(--grey);color:var(--white)}
.difference .heading{position:absolute;left:0;width:1200px;top:92px;text-align:center;font-size:38px;font-weight:300}
.feature{position:absolute;top:180px;width:290px;text-align:center}
.feature svg{display:block;margin:0 auto;height:70px}
.feature h3{margin-top:26px;font-size:21px;font-weight:700}
.feature p{margin-top:12px;font-size:16px;line-height:19px;font-weight:600}
.btn-outline{border:1px solid var(--white);color:var(--white);display:flex;align-items:center;justify-content:center;font-size:16px;font-weight:600}
/* testimonial */
.avatar{left:554px;top:2149px;width:90px;height:90px;border-radius:50%;border:2px solid #999;background:var(--white)}
.avatar span{position:absolute;left:6px;top:6px;width:74px;height:74px;border-radius:50%;background:var(--grey)}
.center{left:0;width:1200px;text-align:center}
/* promo */
.promo{left:0;top:2462px;width:1200px;height:265px;background:var(--green)}
.promo-car{left:0;top:2453px;width:557px;height:324px;border-radius:20% 40% 35% 10%;background:linear-gradient(180deg,#c2c2c6,#8d8d93 70%,#5b5b60)}
.promo-list{left:627px;top:2542px;list-style:none;font-size:16px;font-weight:600;color:var(--white);line-height:23px}
.promo-list li{display:flex;align-items:center;gap:10px}
.promo-list li::before{content:"";border-top:7px solid transparent;border-bottom:7px solid transparent;border-left:12px solid var(--white)}
/* footer */
.footer{left:0;top:2845px;width:1200px;height:443px;background:var(--dark);color:#ccc}
.footer h4{position:absolute;font-size:24px;font-weight:400;color:#ddd}
.footer ul{position:absolute;list-style:none;font-size:16px;line-height:23px}
.footer .contact li{display:flex;align-items:center;gap:12px;margin-bottom:5px}
.footer .contact svg{width:16px;height:16px}
.bottombar{left:0;top:3288px;width:1200px;height:47px;background:var(--darker);color:#aaa;font-size:11px;display:flex;align-items:center;justify-content:center}
</style>
</head>
<body>

<!-- top bar -->
<div class="abs topbar">
  <div class="contact-item" style="left:100px">
    <svg width="16" height="16" viewBox="0 0 24 24"><path fill="#fff" d="M6.6 10.8a15 15 0 0 0 6.6 6.6l2.2-2.2c.3-.3.7-.4 1-.2 1.1.4 2.3.6 3.6.6.6 0 1 .4 1 1V20c0 .6-.4 1-1 1A17 17 0 0 1 3 4c0-.6.4-1 1-1h3.5c.6 0 1 .4 1 1 0 1.3.2 2.5.6 3.6.1.3 0 .7-.2 1z"/></svg>
    555.014.2290
  </div>
  <div class="contact-item" style="left:272px">
    <svg width="18" height="13" viewBox="0 0 18 13"><rect x=".5" y=".5" width="17" height="12" fill="none" stroke="#fff"/><path d="M.5.5 9 7l8.5-6.5" fill="none" stroke="#fff"/></svg>
    info@favorzo.com
  </div>
  <div class="social" style="left:798px"><span></span><span></span><span></span><span></span></div>
  <div class="login">Login ●</div>
  <div class="register">Register ■</div>
</div>

<!-- header -->
<div class="abs logo" style="left:100px;top:58px">
  <div class="mark"></div>
  <div class="name">Favorzo</div>
</div>
<nav class="abs nav">
  <a class="active" style="left:0">Home</a>
  <a style="left:90px">Services ⌵</a>
  <a style="left:217px">About</a>
  <a style="left:320px">Contact</a>
  <a style="left:436px">News</a>
</nav>
<div class="abs btn-offer">Get an Offer</div>

<!-- hero -->
<div class="abs hero" role="img" aria-label="Photo of a white electric sedan parked on grass in front of trees"></div>
<div class="abs hero-car" role="img" aria-label="White sedan"></div>
<svg class="abs" style="left:0;top:690px" width="1200" height="140" viewBox="0 0 1200 140">
  <path d="M0 18 C180 -10 360 40 520 90 C700 140 950 120 1200 20 L1200 140 L0 140 Z" fill="var(--green-light)"/>
  <path d="M0 40 C200 0 380 60 560 100 C760 140 980 110 1200 18 L1200 140 L0 140 Z" fill="var(--green)"/>
  <path d="M0 140 L0 140 C120 60 300 60 520 110 C760 160 980 120 1200 26 L1200 140 Z" fill="var(--white)"/>
</svg>
<div class="abs hero-title">Sell your car quickly!</div>
<div class="abs field" style="left:117px;top:295px;width:322px;height:44px">Make<span class="caret"></span></div>
<div class="abs field" style="left:117px;top:355px;width:322px;height:44px">Model<span class="caret"></span></div>
<div class="abs field" style="left:117px;top:414px;width:152px;height:44px">Year<span class="caret"></span></div>
<div class="abs field" style="left:286px;top:414px;width:153px;height:44px">Price</div>
<div class="abs field" style="left:117px;top:474px;width:322px;height:45px">Email</div>
<div class="abs btn-quote">Quote Me</div>

<!-- cash offers -->
<div class="abs section-title" style="left:117px;top:838px">Cash Offers Made Daily!</div>
<div class="abs rule" style="left:117px;top:892px;width:687px"></div>
<div class="abs" style="left:117px;top:904px;font-size:14px;font-weight:300;color:#777">Receive cash on the spot for your vehicle! It doesn't matter how bad of shape it is in, we'll take it!</div>

<svg class="abs arrow" style="left:60px;top:1076px" viewBox="0 0 24 48"><path d="M22 2 2 24l20 22" fill="none" stroke="#888" stroke-width="2"/></svg>
<svg class="abs arrow" style="left:1117px;top:1076px" viewBox="0 0 24 48"><path d="M2 2l20 22L2 46" fill="none" stroke="#888" stroke-width="2"/></svg>

<div class="abs card" style="left:117px">
  <div class="photo" role="img" aria-label="Photo of a dark blue sedan" style="background:linear-gradient(180deg,#c9cdd0,#3a3f4a 60%,#8a8f8c)"></div>
  <div class="title">2011 Marlow Sedan</div>
  <div class="loc"><svg width="12" height="16" viewBox="0 0 12 16"><path d="M6 0a6 6 0 0 0-6 6c0 4.5 6 10 6 10s6-5.5 6-10a6 6 0 0 0-6-6zm0 8.5A2.5 2.5 0 1 1 6 3.5a2.5 2.5 0 0 1 0 5z" fill="#999"/></svg>Fairhaven, RI</div>
  <div class="stars">★★★★<b>★</b></div>
  <div class="sep"></div>
  <div class="meta" style="top:262px">▭ 5 comments<br>◉ 151 views</div>
  <div class="price"><sup>$</sup>280</div>
</div>
<div class="abs card" style="left:368px">
  <div class="photo" role="img" aria-label="Photo of a red coupe" style="background:linear-gradient(180deg,#6f7a55,#c8262a 55%,#9a9a8e)"></div>
  <div class="title">2011 Marlow Sedan</div>
  <div class="loc"><svg width="12" height="16" viewBox="0 0 12 16"><path d="M6 0a6 6 0 0 0-6 6c0 4.5 6 10 6 10s6-5.5 6-10a6 6 0 0 0-6-6zm0 8.5A2.5 2.5 0 1 1 6 3.5a2.5 2.5 0 0 1 0 5z" fill="#999"/></svg>Fairhaven, RI</div>
  <div class="stars">★★★★<b>★</b></div>
  <div class="sep"></div>
  <div class="meta" style="top:262px">▭ 5 comments<br>◉ 151 views</div>
  <div class="price"><sup>$</sup>280</div>
</div>
<div class="abs card" style="left:620px">
  <div class="photo" role="img" aria-label="Photo of a grey sedan in a driveway" style="background:linear-gradient(180deg,#b7c1b0,#56595a 55%,#7f836f)"></div>
  <div class="title">2011 Marlow Sedan</div>
  <div class="loc"><svg width="12" height="16" viewBox="0 0 12 16"><path d="M6 0a6 6 0 0 0-6 6c0 4.5 6 10 6 10s6-5.5 6-10a6 6 0 0 0-6-6zm0 8.5A2.5 2.5 0 1 1 6 3.5a2.5 2.5 0 0 1 0 5z" fill="#999"/></svg>Fairhaven, RI</div>
  <div class="stars">★★★★<b>★</b></div>
  <div class="sep"></div>
  <div class="meta" style="top:262px">▭ 5 comments<br>◉ 151 views</div>
  <div class="price"><sup>$</sup>280</div>
</div>
<div class="abs card" style="left:871px">
  <div class="photo" role="img" aria-label="Photo of a red pickup truck" style="background:linear-gradient(180deg,#4f7a46,#c4262b 50%,#6d8c52)"></div>
  <div class="title">2011 Marlow Sedan</div>
  <div class="loc"><svg width="12" height="16" viewBox="0 0 12 16"><path d="M6 0a6 6 0 0 0-6 6c0 4.5 6 10 6 10s6-5.5 6-10a6 6 0 0 0-6-6zm0 8.5A2.5 2.5 0 1 1 6 3.5a2.5 2.5 0 0 1 0 5z" fill="#999"/></svg>Fairhaven, RI</div>
  <div class="stars">★★★★<b>★</b></div>
  <div class="sep"></div>
  <div class="meta" style="top:262px">▭ 5 comments<br>◉ 151 views</div>
  <div class="price"><sup>$</sup>280</div>
</div>

<!-- difference -->
<section class="abs difference">
  <div class="heading">The Favorzo Difference</div>
  <div class="feature" style="left:114px">
    <svg viewBox="0 0 70 70" width="70"><circle cx="35" cy="28" r="24" fill="#fff"/><text x="35" y="39" text-anchor="middle" font-family="Open Sans,sans-serif" font-weight="700" font-size="30" fill="var(--grey)">$</text><path d="M4 56v10h62V56" fill="none" stroke="#fff" stroke-width="4"/></svg>
    <h3>Cash on the spot!</h3>
    <p>Offering check, QuickSend, PayLink, or CoinPost instant transfers for your car! Of course, we also offer a standard check as well. Our professional drivers will hand deliver your check.</p>
  </div>
  <div class="feature" style="left:454px">
    <svg viewBox="0 0 50 70" width="50"><path d="M2 2h34l12 12v54H2z" fill="#fff"/><g stroke="var(--grey)" stroke-width="2"><path d="M10 24h30M10 30h30M10 36h30M10 42h30M10 48h30M10 54h30"/></g></svg>
    <h3>Professional title handlers</h3>
    <p>Have an issue with the title? No Problem. Our certified, professional drivers are well trained and can help you transfer that title in no time. We've been doing this quite a while.</p>
  </div>
  <div class="feature" style="left:817px">
    <svg viewBox="0 0 62 70" width="62"><path d="M12 24l5-12h28l5 12h6v20h-4v8h-8v-8H18v8h-8v-8H6V24z" fill="#fff"/><path d="M18 22l3-7h20l3 7z" fill="var(--grey)"/><circle cx="15" cy="34" r="4" fill="var(--grey)"/><circle cx="47" cy="34" r="4" fill="var(--grey)"/></svg>
    <h3>We buy all car types</h3>
    <p>Every scrap car has value, even if you might not think so. We're happy to take them off your hands and recycle them. Saving our planet is a priority and one less car wasting away helps!</p>
  </div>
  <div class="abs btn-outline" style="left:498px;top:480px;width:204px;height:48px">Hire a Professional</div>
</section>

<!-- testimonial -->
<div class="abs section-title center" style="top:2060px">Committed to Excellence</div>
<div class="abs avatar"><span></span></div>
<div class="abs center" style="top:2291px;font-size:17px;font-weight:600;color:#777">Fast and Simple.</div>
<div class="abs center" style="top:2327px;font-size:20px;font-weight:300;color:#777">"Called in the morning. They came, wrote me a check, and took my car before I finished my lunch."</div>
<div class="abs center" style="top:2380px;font-size:14px;font-style:italic;color:#888">Dale Morrow</div>
<svg class="abs arrow" style="left:60px;top:2316px" viewBox="0 0 24 48"><path d="M22 2 2 24l20 22" fill="none" stroke="#888" stroke-width="2"/></svg>
<svg class="abs arrow" style="left:1117px;top:2316px" viewBox="0 0 24 48"><path d="M2 2l20 22L2 46" fill="none" stroke="#888" stroke-width="2"/></svg>

<!-- promo -->
<div class="abs promo"></div>
<div class="abs promo-car" role="img" aria-label="Photo of a silver luxury coupe"></div>
<div class="abs" style="left:627px;top:2480px;font-size:38px;font-weight:300;color:var(--white)">Committed to Excellence</div>
<ul class="abs promo-list">
  <li>Trusted Buyer</li>
  <li>Thousands of Happy Sellers</li>
  <li>Get an offer instantly Online!</li>
</ul>
<div class="abs btn-outline" style="left:629px;top:2641px;width:200px;height:52px;font-size:19px;font-weight:300">Get an Offer</div>
<div class="abs" style="left:631px;top:2733px;font-size:10px;color:#bbb">We don't sell your information, we will only contact you about your car.</div>

<!-- footer -->
<footer class="abs footer">
  <h4 style="left:105px;top:80px">Favorzo</h4>
  <div class="abs rule" style="left:105px;top:118px;width:465px;background:#888;height:1px"></div>
  <ul style="left:105px;top:138px">
    <li>Home</li><li>Services</li><li>About</li><li>Contact</li><li>News</li><li>Get and offer</li><li>Register</li>
  </ul>
  <ul style="left:260px;top:138px">
    <li>Junk Yards That Take Cars Without Title</li><li>Scrap My Car For Money</li><li>Fast Cash for Junk Cars</li><li>Free Car Removal</li><li>Scrap Car Removal</li><li>Sell My Junk Car for Cash Today</li><li>Junk Cars Bought</li>
  </ul>
  <h4 style="left:607px;top:80px">Contact</h4>
  <div class="abs rule" style="left:607px;top:118px;width:335px;background:#888;height:1px"></div>
  <ul class="contact" style="left:607px;top:138px">
    <li><svg viewBox="0 0 24 24"><path fill="#aaa" d="M6.6 10.8a15 15 0 0 0 6.6 6.6l2.2-2.2c.3-.3.7-.4 1-.2 1.1.4 2.3.6 3.6.6.6 0 1 .4 1 1V20c0 .6-.4 1-1 1A17 17 0 0 1 3 4c0-.6.4-1 1-1h3.5c.6 0 1 .4 1 1 0 1.3.2 2.5.6 3.6.1.3 0 .7-.2 1z"/></svg>555.014.2290</li>
    <li><svg viewBox="0 0 18 13"><rect x=".5" y=".5" width="17" height="12" fill="none" stroke="#aaa"/><path d="M.5.5 9 7l8.5-6.5" fill="none" stroke="#aaa"/></svg>info@favorzo.com</li>
    <li><svg viewBox="0 0 12 16"><path d="M6 0a6 6 0 0 0-6 6c0 4.5 6 10 6 10s6-5.5 6-10a6 6 0 0 0-6-6zm0 8.5A2.5 2.5 0 1 1 6 3.5a2.5 2.5 0 0 1 0 5z" fill="#aaa"/></svg>Complete Address Elmwood, Vermont</li>
    <li><svg viewBox="0 0 16 16"><circle cx="8" cy="8" r="7" fill="none" stroke="#aaa" stroke-width="1.5"/><path d="M1 8h14M8 1c3 3 3 11 0 14M8 1c-3 3-3 11 0 14" fill="none" stroke="#aaa"/></svg>www.favorzo.com</li>
  </ul>
  <div class="abs logo" style="left:988px;top:148px">
    <div class="mark" style="background:#777"></div>
    <div class="name" style="color:#999;font-size:24px">Favorzo</div>
  </div>
  <div class="abs" style="left:984px;top:278px;display:flex;gap:14px">
    <span style="width:18px;height:18px;background:#999;border-radius:3px"></span>
    <span style="width:18px;height:18px;background:#999;border-radius:3px"></span>
    <span style="width:18px;height:18px;background:#999;border-radius:3px"></span>
    <span style="width:18px;height:18px;background:#999;border-radius:3px"></span>
  </div>
  <div class="abs" style="left:105px;top:324px;width:992px;height:1px;background:#777"></div>
  <div class="abs" style="left:479px;top:352px;width:104px;height:46px;background:#3a3a3a;border-radius:4px" role="img" aria-label="Payment methods badge"></div>
  <div class="abs" style="left:623px;top:352px;width:95px;height:46px;background:#1f4e79;border-radius:3px" role="img" aria-label="Business accreditation badge"></div>
</footer>
<div class="abs bottombar">© 2020 Favorzo, LLC. All rights are reserved.</div>

</body>
</html>
```